Flyer-Design für Werkstatt-Umzug
Vielen lieben Dank für das tolle Design, sowie die schnelle Bearbeitung. Auch nach dem Zuschlag ein toller Service.
Zielgruppe
Wir sind eine kleine Kfz-Werkstatt und ziehen nun um. Dazu soll ein Info-Flyer ausgelegt werden und mit in Rechnungen & Briefe. Zielgruppe sind neben der deutschen Kundschaft, auch viele dänische Kunden.
Aufgabenstellung
Wir dachten einen zweiseitigen Flyer (DIN lang), vorne Deutsch, hinten Dänisch. Wir dachten an folgenden Text:
Deutsch: Ab Januar 2018 begrüßen wir Sie in unserer neuen Werkstatt
Homepage www.kfz-technik-olmer.de
Dänisch: Januar 2018 er alle hjertelig velkommen i hvores nye værksted:

```html
<!DOCTYPE html>
<html lang="de">
<head>
<meta charset="utf-8">
<title>Umzugsflyer Werkstatt</title>
<link href="https://fonts.googleapis.com/css2?family=Arimo:wght@400;700&display=swap" rel="stylesheet">
<style>
  :root {
    --green: #14cc14;
    --green-dark: #0a9e0a;
    --red: #e30613;
    --red-dark: #b8000c;
    --white: #ffffff;
    --ink: #111111;
    --paper-shade: #ececec;
    --stage: #dedede;
    --flag-black: #111111;
    --flag-red: #dd0000;
    --flag-gold: #ffce00;
    --figure-light: #f2f2f2;
    --figure-mid: #d9d9d9;
  }
  * { box-sizing: border-box; margin: 0; padding: 0; }
  html, body { width: 1200px; height: 1026px; overflow: hidden; }
  body { background: var(--stage); font-family: "Arimo", Arial, sans-serif; color: var(--ink); position: relative; }

  .flyer {
    position: absolute; left: 40px; width: 1120px; height: 470px;
    background: linear-gradient(180deg, var(--white) 55%, var(--paper-shade) 100%);
    overflow: hidden; box-shadow: 0 4px 14px rgba(0,0,0,.18);
  }
  .flyer--danish { top: 28px; }
  .flyer--german { top: 528px; }

  .band { position: absolute; left: 0; top: 40px; width: 100%; height: 140px; }
  .flyer--german .band { background: linear-gradient(180deg, var(--green) 0%, var(--green) 70%, var(--green-dark) 100%); }
  .flyer--danish .band { background: linear-gradient(180deg, var(--red) 0%, var(--red) 70%, var(--red-dark) 100%); }

  .service-icons { position: absolute; left: 50px; top: 72px; display: flex; gap: 14px; z-index: 3; }
  .service-icons svg { width: 78px; height: 78px; display: block; }

  .band__url { position: absolute; right: 110px; top: 52px; color: var(--white); font-weight: 700; font-size: 17px; letter-spacing: .3px; z-index: 3; }
  .band__headline { position: absolute; right: 100px; top: 88px; color: var(--white); font-weight: 700; font-size: 58px; letter-spacing: 2px; z-index: 3; line-height: 1; }

  .flag { position: absolute; right: 0; top: 0; width: 78px; height: 200px; z-index: 2; }

  .illustration {
    position: absolute; border-radius: 40px; z-index: 1;
    background: radial-gradient(ellipse at 50% 40%, var(--figure-light) 0%, var(--figure-mid) 60%, rgba(216,168,104,.35) 100%);
  }
  .flyer--german .illustration { left: 60px; top: 20px; width: 440px; height: 430px; }
  .flyer--danish .illustration--carrier { left: 330px; top: 20px; width: 240px; height: 430px; }
  .flyer--danish .illustration--trolley { left: 880px; top: 230px; width: 210px; height: 200px; }

  .message { position: absolute; text-align: center; z-index: 3; }
  .flyer--german .message { left: 540px; top: 200px; width: 420px; }
  .flyer--danish .message { left: 560px; top: 200px; width: 320px; }
  .message__date { font-weight: 700; font-size: 52px; line-height: 1.1; white-space: nowrap; }
  .flyer--german .message__date { color: var(--green); }
  .flyer--danish .message__date { color: var(--red); }
  .message__welcome { font-size: 25px; line-height: 1.15; margin-top: 12px; }
  .message__address { font-size: 27px; line-height: 1.15; margin-top: 22px; }

  .brand-seal {
    position: absolute; left: 950px; top: 300px; width: 210px; height: 210px; border-radius: 50%;
    border: 6px solid var(--green); background: var(--white); z-index: 3;
    display: flex; justify-content: center; align-items: flex-start; padding-top: 62px; padding-right: 30px;
  }
  .brand-seal span { font-weight: 700; font-size: 20px; color: var(--ink); white-space: nowrap; }

  .map {
    position: absolute; left: 150px; bottom: -150px; width: 300px; height: 300px; border-radius: 50%;
    border: 6px solid var(--red); z-index: 3;
    background: linear-gradient(135deg, #cfe7c9 0%, #eeeae2 55%, #bfdcb6 100%);
  }
</style>
</head>
<body>

  <section class="flyer flyer--danish" lang="da">
    <div class="band"></div>
    <svg class="flag" viewBox="0 0 78 200" aria-hidden="true">
      <rect width="78" height="200" fill="var(--red)"/>
      <rect x="0" y="70" width="78" height="22" fill="var(--white)"/>
      <rect x="22" y="0" width="22" height="200" fill="var(--white)"/>
    </svg>
    <div class="service-icons" aria-hidden="true">
      <svg viewBox="0 0 80 80"><circle cx="40" cy="40" r="38" fill="var(--white)"/><path d="M22 58 L46 34 M44 22 a12 12 0 1 0 14 14 l-6 -2 -4 -6 z" stroke="var(--red)" stroke-width="8" fill="none" stroke-linecap="round"/></svg>
      <svg viewBox="0 0 80 80"><circle cx="40" cy="40" r="38" fill="var(--white)"/><path d="M18 50 L24 30 H56 L62 50 Z M18 50 H62 V56 H18 Z" fill="var(--red)"/><rect x="28" y="34" width="24" height="10" fill="var(--white)"/></svg>
      <svg viewBox="0 0 80 80"><circle cx="40" cy="40" r="38" fill="var(--white)"/><path d="M20 28 H58 V38 H44 L38 60 H30 L34 38 H20 Z M52 18 H60 V28 H52 Z" fill="var(--red)"/></svg>
    </div>
    <div class="band__url">www.werkstatt-lindholm.de</div>
    <div class="band__headline">VI FLYTNING…</div>
    <div class="illustration illustration--carrier" role="img" aria-label="Illustration: weiße 3D-Figur trägt einen Umzugskarton"></div>
    <div class="illustration illustration--trolley" role="img" aria-label="Illustration: zwei 3D-Figuren mit Sackkarre und Kartons"></div>
    <div class="map" role="img" aria-label="Stadtplanausschnitt mit Standort der neuen Werkstatt"></div>
    <div class="message">
      <p class="message__date">Januar 2018</p>
      <p class="message__welcome">er alle hjertelig velkommen<br>i hvores nye værksted</p>
      <p class="message__address">Am Werkhof 7b<br>24999 Wiesbrook<br>Tyskland</p>
    </div>
  </section>

  <section class="flyer flyer--german">
    <div class="band"></div>
    <svg class="flag" viewBox="0 0 78 200" aria-hidden="true">
      <rect y="0" width="78" height="67" fill="var(--flag-black)"/>
      <rect y="67" width="78" height="66" fill="var(--flag-red)"/>
      <rect y="133" width="78" height="67" fill="var(--flag-gold)"/>
    </svg>
    <div class="service-icons" aria-hidden="true">
      <svg viewBox="0 0 80 80"><circle cx="40" cy="40" r="38" fill="var(--white)"/><path d="M22 58 L46 34 M44 22 a12 12 0 1 0 14 14 l-6 -2 -4 -6 z" stroke="var(--green)" stroke-width="8" fill="none" stroke-linecap="round"/></svg>
      <svg viewBox="0 0 80 80"><circle cx="40" cy="40" r="38" fill="var(--white)"/><path d="M18 50 L24 30 H56 L62 50 Z M18 50 H62 V56 H18 Z" fill="var(--green)"/><rect x="28" y="34" width="24" height="10" fill="var(--white)"/></svg>
      <svg viewBox="0 0 80 80"><circle cx="40" cy="40" r="38" fill="var(--white)"/><path d="M20 28 H58 V38 H44 L38 60 H30 L34 38 H20 Z M52 18 H60 V28 H52 Z" fill="var(--green)"/></svg>
    </div>
    <div class="band__url">www.werkstatt-lindholm.de</div>
    <div class="band__headline">WIR ZIEHEN UM…</div>
    <div class="illustration" role="img" aria-label="Illustration: weiße 3D-Figuren tragen Umzugskartons und schieben eine Sackkarre"></div>
    <div class="message">
      <p class="message__date">ab Januar 2018</p>
      <p class="message__welcome">begrüßen wir Sie in unserer<br>neuen Werkstatt</p>
      <p class="message__address">Am Werkhof 7b<br>24999 Wiesbrook</p>
    </div>
    <div class="brand-seal"><span>KFZ LINDHOLM</span></div>
  </section>

</body>
</html>
```